Email Signature Design (GIF)

I need an Email Signature designed, In a GIF format. The following Excel File and Logo Image should be applied. The Logo on the left and the Fixed "Supplying" and rotating words amongst the variety appears on the right.
e.g. "(VT LOGO) Supplying (Variant)" . Please us the Quorvix screenshots, only as an example.

Target Market(s)

Our current customer base (Construction)

Industry/Entity Type

Construction

Font styles to use
Sans Serif

Requirements
Must have
• My project Must follow the instructions in the Project description

```html
<!DOCTYPE html>
<html lang="en">
<head>
<meta charset="utf-8">
<title>Vantor Terra – Email Signature</title>
<link href="https://fonts.googleapis.com/css2?family=Montserrat:wght@500;800&display=swap" rel="stylesheet">
<style>
  :root {
    --backdrop: #0394c8;
    --navy: #161c45;
    --paper: #ffffff;
    --orange: #ee7b45;
    --ink: #111111;
  }
  * { margin: 0; padding: 0; box-sizing: border-box; }
  html, body { width: 1200px; height: 1200px; overflow: hidden; }
  body { background: var(--backdrop); font-family: "Montserrat", Arial, sans-serif; position: relative; }

  .signature { position: absolute; left: 235px; top: 441px; width: 731px; height: 244px; }
  .signature-frame { position: absolute; inset: 0; width: 100%; height: 100%; }

  .rule { position: absolute; left: 87px; width: 568px; height: 2px; background: var(--orange); border-radius: 1px; }
  .rule-top { top: 49px; }
  .rule-bottom { top: 197px; }
  .divider { position: absolute; left: 218px; top: 72px; width: 2px; height: 108px; background: var(--orange); border-radius: 1px; }

  .brand-name {
    position: absolute; left: 85px; top: 92px; width: 115px;
    font-weight: 800; font-size: 17px; line-height: 1.05; color: var(--navy); text-align: center;
  }

  .social { position: absolute; left: 88px; top: 157px; display: flex; gap: 4.5px; }
  .social-dot { width: 22px; height: 22px; border-radius: 50%; background: var(--navy); }

  .product-list { position: absolute; list-style: none; }
  .product-list li { position: absolute; left: 0; height: 16px; display: flex; align-items: center; white-space: nowrap; font-weight: 500; font-size: 11.5px; color: var(--ink); }
  .product-list .mark { width: 14px; height: 14px; border-radius: 50%; border: 2px solid var(--orange); margin-left: 6px; }
  .product-list .fixed { position: absolute; left: 38px; }
  .product-list .variant { position: absolute; }
  .list-left { left: 245px; top: 0; }
  .list-left .variant { left: 101px; }
  .list-right { left: 468px; top: 0; }
  .list-right .fixed { left: 36px; }
  .list-right .variant { left: 99px; }
</style>
</head>
<body>
  <section class="signature" aria-label="Vantor Terra email signature">
    <svg class="signature-frame" viewBox="0 0 731 244" preserveAspectRatio="none" aria-hidden="true">
      <rect width="731" height="244" fill="var(--navy)"/>
      <path d="M35 0 H574 C600 20 625 33 653 32 C680 31 700 30 703 37 V244 H167 C140 222 115 208 88 209 C60 210 36 212 35 204 Z" fill="var(--paper)"/>
    </svg>

    <div class="rule rule-top"></div>
    <div class="rule rule-bottom"></div>
    <div class="divider"></div>

    <div class="brand-name">Vantor Terra</div>

    <div class="social" aria-label="Social links">
      <span class="social-dot"></span>
      <span class="social-dot"></span>
      <span class="social-dot"></span>
      <span class="social-dot"></span>
    </div>

    <ul class="product-list list-left">
      <li style="top:70px"><span class="mark"></span><span class="fixed">Supplying</span><span class="variant">Sand</span></li>
      <li style="top:86px"><span class="mark"></span><span class="fixed">Supplying</span><span class="variant">Agg</span></li>
      <li style="top:104px"><span class="mark"></span><span class="fixed">Supplying</span><span class="variant">e</span></li>
      <li style="top:120px"><span class="mark"></span><span class="fixed">Supplying</span><span class="variant">Road Base</span></li>
      <li style="top:136px"><span class="mark"></span><span class="fixed">Supplying</span><span class="variant">Soils</span></li>
      <li style="top:152px"><span class="mark"></span><span class="fixed">Supplying</span><span class="variant">Stabilised Sand</span></li>
      <li style="top:168px"><span class="mark"></span><span class="fixed">Supplying</span><span class="variant">Ballast</span></li>
    </ul>

    <ul class="product-list list-right">
      <li style="top:70px"><span class="mark"></span><span class="fixed">Supplying</span><span class="variant">Bedding Sand</span></li>
      <li style="top:86px"><span class="mark"></span><span class="fixed">Supplying</span><span class="variant">Mulch</span></li>
      <li style="top:103px"><span class="mark"></span><span class="fixed">Supplying</span><span class="variant">Select Fill</span></li>
      <li style="top:120px"><span class="mark"></span><span class="fixed">Supplying</span><span class="variant">Gabion Spalls</span></li>
      <li style="top:136px"><span class="mark"></span><span class="fixed">Supplying</span><span class="variant">Glass Sand</span></li>
      <li style="top:152px"><span class="mark"></span><span class="fixed">Supplying</span><span class="variant">Stabilised Base</span></li>
    </ul>
  </section>
</body>
</html>
```